New Business Card

We need to refresh our business cards. We designed these ourselves and we have no graphic design experience. We would like to find a new business card design that is professional and unique. We are an auto finance company. Feel free to play with the logo, but we would like to keep the eye very present on the card. Our corporate colors are green, grey, and white.
Green - RGB - 168,215,27; HEX - #AADD22
Grey - RGB - 196,196,196; HEX - #C4C4C4
Updates
Need to upload the vector file to finalize the project. The last logo was for a jpeg that didn't stretch well.
Industry/Entity Type
Financial Service
Contact Information for Business Card
Honestly don't know...I need your help!

```html
<!DOCTYPE html>
<html lang="en">
<head>
<meta charset="utf-8">
<title>Brightway Capital – Business Card</title>
<link rel="stylesheet" href="https://fonts.googleapis.com/css2?family=Yanone+Kaffeesatz:wght@400;500&display=swap">
<style>
  :root {
    --green: #aadd22;
    --green-ink: #8cc21a;
    --grey: #c4c4c4;
    --grey-dark: #9a9a9a;
    --white: #ffffff;
    --backdrop: #eceeee;
  }
  * { box-sizing: border-box; margin: 0; padding: 0; }
  html, body {
    width: 1200px; height: 980px; overflow: hidden;
    background: var(--backdrop);
  }
  .card {
    position: absolute; left: 100px; top: 220px;
    width: 1000px; height: 540px;
    background: var(--white);
    box-shadow: 0 14px 40px rgba(0,0,0,.14);
    overflow: hidden;
    font-family: "Yanone Kaffeesatz", "Arial Narrow", sans-serif;
    color: var(--green-ink);
  }
  .card__rule-vertical {
    position: absolute; left: 485px; top: 0; width: 7px; height: 100%;
    background: var(--green);
  }
  .card__block {
    position: absolute; left: 492px; right: 0; background: var(--grey);
  }
  .card__block--top { top: 0; height: 170px; }
  .card__block--bottom { top: 362px; bottom: 0; }
  .brand-band {
    position: absolute; left: 390px; right: -2px; top: 170px; height: 192px;
    background: var(--white);
    border-radius: 96px 0 0 96px;
    border: 2px solid #e2e2e2; border-right: none;
    box-shadow: -2px 3px 6px rgba(0,0,0,.08);
    display: flex; align-items: center; gap: 26px;
    padding-left: 60px;
  }
  .brand-band__dot {
    width: 74px; height: 74px; border-radius: 50%;
    background: var(--grey); flex: none;
  }
  .brand-band__name {
    font-size: 66px; font-weight: 500; color: var(--green-ink);
    letter-spacing: .5px; white-space: nowrap;
  }
  .identity {
    position: absolute; left: 55px; width: 325px; top: 90px; text-align: center;
  }
  .identity__name { font-size: 50px; font-weight: 500; line-height: 1; }
  .identity__title { font-size: 32px; font-weight: 400; margin-top: 4px; }
  .card__rule-horizontal {
    position: absolute; left: 55px; top: 215px; width: 325px; height: 3px;
    background: var(--green);
  }
  .contact {
    position: absolute; left: 55px; top: 275px; list-style: none;
  }
  .contact__item {
    display: flex; align-items: center; gap: 14px;
    font-size: 31px; height: 56px;
  }
  .contact__icon { width: 36px; height: 36px; flex: none; }
</style>
</head>
<body>
  <article class="card">
    <div class="card__block card__block--top"></div>
    <div class="card__block card__block--bottom"></div>
    <div class="card__rule-vertical"></div>

    <div class="identity">
      <h1 class="identity__name">Daniel Hart</h1>
      <p class="identity__title">President</p>
    </div>
    <div class="card__rule-horizontal"></div>

    <ul class="contact">
      <li class="contact__item">
        <svg class="contact__icon" viewBox="0 0 36 36" fill="none" stroke="#8cc21a" stroke-width="2.4">
          <rect x="11" y="4" width="14" height="28" rx="2.5"/>
          <line x1="15" y1="27" x2="21" y2="27"/>
        </svg>
        555-214-0187
      </li>
      <li class="contact__item">
        <svg class="contact__icon" viewBox="0 0 36 36">
          <rect x="3" y="9" width="30" height="19" fill="#8cc21a"/>
          <polyline points="3,9 18,20 33,9" fill="none" stroke="#fff" stroke-width="2"/>
        </svg>
        hello@brightwaycap.com
      </li>
      <li class="contact__item">
        <svg class="contact__icon" viewBox="0 0 36 36" fill="none" stroke="#8cc21a" stroke-width="2.2">
          <circle cx="18" cy="18" r="14"/>
          <ellipse cx="18" cy="18" rx="6" ry="14"/>
          <line x1="4" y1="18" x2="32" y2="18"/>
          <line x1="6" y1="11" x2="30" y2="11"/>
          <line x1="6" y1="25" x2="30" y2="25"/>
        </svg>
        www.brightwaycap.com
      </li>
    </ul>

    <div class="brand-band">
      <span class="brand-band__dot"></span>
      <span class="brand-band__name">Brightway Capital</span>
    </div>
  </article>
</body>
</html>
```